Workplace Safety Consultancy Business needs business card design

We need a business card for a new business providing workplace health and safety consulting called 'Worksure Guard'. We will be providing small to medium sized businesses assistance with OH&S and HR matters to ensure that their employees and the public are safe in the workplace and that they are meeting their legislative requirements. Would like to see the words 'practical workplace safety solutions' on the card. Personal details on the back. It needs to be clean, smart and professional (no fluff). Would like to see a simple logo if possible as well. Have been looking at orange and black, but open to other ideas.
Updates
Thank you to those to have created designs for us so far! We are really impressed with the impact of the black and orange having now seen it. Would be great if any further designs used those colours. Cheers.

Thank you to everyone that submitted a design. Your work is of the highest quality and we had a hard decision deciding. Sorry if we didn't choose your design, but it just came down to the one that stood out to us personally. Cheers.

Target Market(s)
Small-Medium business owners in Queensland, Australia. Age 25-60 male and female. Initially targeting those in the trade type industries
Industry/Entity Type
Health
Look and feel
Each slider illustrates characteristics of the customer's brand and the style your logo design should communicate.

```html
<!DOCTYPE html>
<html lang="en">
<head>
<meta charset="utf-8">
<title>Worksure Guard – Business Card</title>
<link rel="stylesheet" href="https://fonts.googleapis.com/css2?family=Open+Sans:ital,wght@0,300;0,400;0,700;0,800;1,400&display=swap">
<style>
  :root {
    --ink: #231f20;
    --card-black: #252324;
    --safety-orange: #ef5a24;
    --mark-grey: #8a8a8a;
    --paper-white: #ffffff;
    --backdrop: #ecebe8;
  }
  * { margin: 0; padding: 0; box-sizing: border-box; }
  html, body {
    width: 1200px;
    height: 900px;
    overflow: hidden;
    background: var(--backdrop);
    font-family: "Open Sans", Arial, sans-serif;
  }
  .sheet {
    position: relative;
    width: 1200px;
    height: 900px;
  }
  .card {
    position: absolute;
    left: 280px;
    width: 640px;
    height: 392px;
    overflow: hidden;
    box-shadow: 0 6px 18px rgba(0,0,0,0.18);
  }
  .card--back { top: 31px; background: var(--safety-orange); }
  .card--front { top: 477px; background: var(--card-black); }
  .card__shapes {
    position: absolute;
    inset: 0;
    width: 100%;
    height: 100%;
  }
  .brand {
    position: absolute;
    display: flex;
    align-items: center;
    gap: 22px;
  }
  .brand__dot {
    width: 74px;
    height: 74px;
    border-radius: 50%;
    background: var(--mark-grey);
    flex: none;
  }
  .brand__name {
    color: var(--paper-white);
    font-weight: 800;
    font-size: 36px;
    letter-spacing: 0.5px;
    text-transform: uppercase;
    line-height: 1.05;
  }
  .card--back .brand {
    left: 40px;
    top: 110px;
    width: 280px;
    flex-direction: column;
    align-items: flex-start;
    gap: 24px;
  }
  .card--back .brand__name { font-size: 34px; }
  .card--front .brand { left: 140px; top: 140px; }
  .holder {
    position: absolute;
    right: 34px;
    top: 22px;
    color: var(--ink);
    font-weight: 700;
    font-size: 22px;
  }
  .contact {
    position: absolute;
    right: 30px;
    top: 196px;
    list-style: none;
    text-align: right;
    color: var(--ink);
    font-weight: 300;
    font-size: 15px;
    line-height: 1.8;
    white-space: nowrap;
  }
  .tagline {
    position: absolute;
    right: 26px;
    bottom: 10px;
    color: var(--paper-white);
    font-style: italic;
    font-weight: 400;
    font-size: 33px;
    letter-spacing: -0.3px;
    white-space: nowrap;
  }
</style>
</head>
<body>
<main class="sheet">

  <section class="card card--back" aria-label="Business card, personal details side">
    <svg class="card__shapes" viewBox="0 0 640 392" aria-hidden="true">
      <path fill="var(--card-black)" d="M0 0 H322 Q346 0 346 24 V392 H0 Z"/>
      <path fill="var(--safety-orange)" d="M0 230 H4 Q22 230 22 252 V392 H0 Z"/>
      <path fill="var(--card-black)" d="M346 344 H640 V392 H346 Z"/>
      <path fill="var(--safety-orange)" d="M370 344 H520 Q532 344 532 356 V360 Q532 372 520 372 H382 Q370 372 370 360 Z"/>
    </svg>
    <div class="brand">
      <span class="brand__dot"></span>
      <span class="brand__name">Worksure Guard</span>
    </div>
    <p class="holder">Daniel Ashworth</p>
    <ul class="contact">
      <li>M : 0491 570 156</li>
      <li>E : daniel@worksureguard.com.au</li>
      <li>W : worksureguard.com.au</li>
    </ul>
  </section>

  <section class="card card--front" aria-label="Business card, brand side">
    <svg class="card__shapes" viewBox="0 0 640 392" aria-hidden="true">
      <path fill="var(--safety-orange)" d="M0 296 H190 Q204 296 204 310 V322 Q204 336 218 336 H408 Q422 336 422 322 V310 Q422 296 436 296 H640 V392 H0 Z"/>
    </svg>
    <div class="brand">
      <span class="brand__dot"></span>
      <span class="brand__name">Worksure Guard</span>
    </div>
    <p class="tagline">practical workplace safety solutions</p>
  </section>

</main>
</body>
</html>
```